Vexorun.co is a multi-sport platform that connects players, clubs, coaches, and organizers in one ecosystem.

Core value:
- Players can instantly find or create games across sports (padel, pickleball, tennis, soccer, etc.)
- Clubs can manage players, classes, staff, and tournaments in one place
- Coaches and organizers can create events and earn money directly through the platform

Key differentiator:
Vexorun is not just for finding games — it is a revenue engine for clubs and sports communities.

Main features to highlight:
- Find and join games instantly
- Create games without coordination friction
- Club management (players, classes, payments)
- Coaches offering lessons and programs
- Tournaments and events between clubs
- Fill empty court time with automated or quick-created events

Business model:
- Free to join
- Platform takes a small fee on transactions (events, classes, subscriptions)

Tagline:
“Let the Games Begin & Pick Your Challenge”

Tone:
Modern, premium, community-driven, and action-oriented.
Focus on simplicity, energy, and real usage scenarios.

Target Market(s)

multi-sport platform that connects players, clubs, coaches, and organizers in one ecosystem.

Industry/Entity Type

Sport

Coding

Coded - Design and coding required

Number of Pages Required

3 page

Requirements
Must have
• Build you the exact Webflow structure (class-by-class export)
Nice to have
• Html y css

```html
<!DOCTYPE html>
<html lang="en">
<head>
<meta charset="utf-8">
<title>Vexorun.co — Let the Games Begin</title>
<link rel="stylesheet" href="https://fonts.googleapis.com/css2?family=Plus+Jakarta+Sans:wght@400;500;600;700;800&family=Manrope:wght@400;500;600;700&display=swap">
<style>
:root{
  --lime:#d4f000;
  --lime-soft:#e4f76a;
  --olive:#3f5d00;
  --olive-deep:#2f4700;
  --ink:#121212;
  --ink-soft:#2a2a2a;
  --muted:#6d6f72;
  --line:#e3e5e7;
  --page:#f6f7f7;
  --band:#eff0f1;
  --white:#ffffff;
  --dark-card:#0e0f10;
}
*{box-sizing:border-box;margin:0;padding:0}
html,body{width:1200px;height:5013px;overflow:hidden}
body{background:var(--page);font-family:"Manrope",sans-serif;color:var(--ink);position:relative}
.heading{font-family:"Plus Jakarta Sans",sans-serif}
a{color:inherit;text-decoration:none}

/* NAV */
.nav{position:absolute;top:0;left:0;width:1200px;height:70px;background:var(--white);border-bottom:1px solid var(--line);display:flex;align-items:center;padding:0 25px}
.nav-brand{font-family:"Plus Jakarta Sans",sans-serif;font-weight:700;font-size:18px}
.nav-links{display:flex;gap:28px;margin-left:48px;font-size:14px;font-weight:600;color:var(--ink-soft);height:70px;align-items:center}
.nav-links a{height:70px;display:flex;align-items:center}
.nav-links .is-active{color:var(--olive);border-bottom:2px solid var(--olive)}
.nav-right{margin-left:auto;display:flex;align-items:center;gap:24px}
.btn{display:inline-flex;align-items:center;justify-content:center;border-radius:999px;font-weight:700;font-family:"Plus Jakarta Sans",sans-serif}
.btn-lime{background:var(--lime);color:var(--ink)}
.nav .btn{height:38px;padding:0 26px;font-size:14px}

/* HERO */
.hero{position:absolute;top:70px;left:0;width:1200px;height:900px}
.hero-tag{position:absolute;left:25px;top:100px;background:var(--lime);font-size:11px;font-weight:700;letter-spacing:.06em;padding:6px 14px;border-radius:999px}
.hero-title{position:absolute;left:25px;top:140px;font-weight:800;font-size:94px;line-height:90px;letter-spacing:-2px;width:560px}
.hero-title .accent{color:var(--olive)}
.hero-text{position:absolute;left:25px;top:632px;width:510px;font-size:18px;line-height:28px;color:var(--ink-soft)}
.hero-actions{position:absolute;left:25px;top:723px;display:flex;gap:18px}
.hero-actions .btn{height:50px;padding:0 32px;font-size:15px}
.btn-grey{background:#e3e4e6;color:var(--ink-soft)}
.hero-tile{position:absolute;border-radius:20px;box-shadow:0 18px 40px rgba(0,0,0,.18);border:4px solid var(--white)}
.tile-a{left:617px;top:134px;width:276px;height:344px;transform:rotate(-1.5deg);background:linear-gradient(160deg,#3f7a4a,#1e5fa8 70%,#2a73c4)}
.tile-b{left:908px;top:82px;width:270px;height:288px;transform:rotate(2deg);background:linear-gradient(170deg,#0f1c2a,#2c5a2e 60%,#3d7a30)}
.tile-c{left:617px;top:510px;width:276px;height:272px;transform:rotate(1.5deg);background:linear-gradient(170deg,#aa6a40,#c86633 55%,#b9582b)}
.tile-d{left:908px;top:378px;width:270px;height:357px;transform:rotate(-1.5deg);background:linear-gradient(170deg,#14323e,#2f6a82 60%,#c9d92a)}

/* PARTNERS */
.partners{position:absolute;top:940px;left:0;width:1200px;height:235px;background:var(--band)}
.partners-label{position:absolute;top:72px;width:100%;text-align:center;font-size:11px;letter-spacing:.3em;color:#9ea1a5;font-weight:600}
.partners-list{position:absolute;top:134px;left:25px;right:25px;display:flex;justify-content:space-between;font-family:"Plus Jakarta Sans",sans-serif;font-weight:800;font-size:21px;color:#55585c;letter-spacing:.03em}
.partners-list span{width:230px;text-align:center}

/* FEATURES */
.card{position:absolute;border-radius:22px;overflow:hidden}
.card-find{left:25px;top:1300px;width:658px;height:464px;background:var(--white)}
.card-find .card-body{position:absolute;left:40px;top:40px;width:300px}
.card-find .photo{position:absolute;left:329px;top:0;width:329px;height:464px;background:linear-gradient(170deg,#1c2f3c,#1c6b9e 55%,#2287c4)}
.card-icon{width:34px;height:34px;display:block}
.card-title{font-family:"Plus Jakarta Sans",sans-serif;font-weight:700;font-size:30px;line-height:36px;margin-top:20px}
.card-text{font-size:15px;line-height:24px;color:var(--muted);margin-top:16px}
.tags{position:absolute;left:40px;bottom:50px;display:flex;gap:10px}
.tag{font-size:11px;font-weight:700;letter-spacing:.06em;background:#eceef0;color:#55585c;padding:8px 14px;border-radius:999px}
.card-manage{left:711px;top:1300px;width:467px;height:464px;background:var(--dark-card);color:var(--white)}
.card-manage .card-body{position:absolute;left:40px;top:55px;right:40px}
.card-manage .card-text{color:#a8abae}
.checks{position:absolute;left:40px;bottom:48px;list-style:none;display:flex;flex-direction:column;gap:18px}
.checks li{display:flex;align-items:center;gap:12px;font-size:13px;font-weight:700;color:var(--lime)}
.card-coach{left:25px;top:1789px;width:464px;height:661px;background:var(--lime)}
.card-coach .card-body{position:absolute;left:40px;top:60px;right:40px}
.card-coach .card-title{color:var(--olive);font-size:34px;line-height:40px}
.card-coach .card-text{color:#5c6e1a}
.card-coach .btn{position:absolute;left:40px;bottom:48px;height:42px;padding:0 28px;background:var(--olive);color:var(--lime);font-size:13px}
.card-create{left:514px;top:1789px;width:664px;height:661px;background:linear-gradient(180deg,#b9c7d2 0%,#8ea3b4 35%,#2f6a95 62%,#0f1f2c 100%)}
.card-create .caption{position:absolute;left:45px;bottom:45px;color:var(--white)}
.card-create .caption h3{font-family:"Plus Jakarta Sans",sans-serif;font-weight:700;font-size:30px}
.card-create .caption p{font-size:15px;margin-top:8px;color:#dde3e8}

/* STEPS */
.steps{position:absolute;top:2680px;left:0;width:1200px;text-align:center}
.section-title{font-family:"Plus Jakarta Sans",sans-serif;font-weight:700;font-size:44px}
.steps .section-sub{font-size:16px;color:var(--muted);margin-top:14px}
.step{position:absolute;top:180px;width:340px;text-align:center}
.step-icon{width:113px;height:113px;border-radius:50%;background:var(--white);margin:0 auto;display:flex;align-items:center;justify-content:center;box-shadow:0 8px 24px rgba(0,0,0,.06)}
.step-icon.is-lime{background:var(--lime)}
.step h4{font-family:"Plus Jakarta Sans",sans-serif;font-weight:700;font-size:18px;margin-top:48px;letter-spacing:.02em}
.step p{font-size:14px;line-height:22px;color:var(--muted);margin-top:14px}

/* ARENA */
.arena{position:absolute;top:3330px;left:25px;width:1153px}
.arena .section-title{font-size:40px}
.arena .section-sub{font-size:15px;color:var(--muted);margin-top:10px}
.arena-link{position:absolute;right:0;top:66px;font-size:13px;font-weight:700;display:flex;align-items:center;gap:8px}
.sport{position:absolute;top:154px;width:266px}
.sport-photo{height:332px;border-radius:20px;position:relative;overflow:hidden}
.sport-badge{position:absolute;top:18px;right:16px;background:rgba(255,255,255,.9);font-size:10px;font-weight:800;letter-spacing:.06em;padding:5px 10px;border-radius:999px}
.sport h5{font-family:"Plus Jakarta Sans",sans-serif;font-weight:700;font-size:22px;margin-top:26px}
.sport p{font-size:13px;color:var(--muted);margin-top:6px}

/* CTA */
.cta{position:absolute;top:4104px;left:25px;width:1153px;height:501px;background:var(--olive);border-radius:30px;text-align:center}
.cta h2{font-family:"Plus Jakarta Sans",sans-serif;font-weight:800;font-size:64px;line-height:66px;color:var(--lime);margin-top:90px}
.cta p{color:#e6ecd8;font-size:17px;line-height:27px;width:460px;margin:24px auto 0}
.cta .btn{height:58px;padding:0 56px;font-size:17px;margin-top:36px}

/* FOOTER */
.footer{position:absolute;top:4700px;left:0;width:1200px;height:313px;background:var(--white);border-top:1px solid var(--line)}
.footer-brand{position:absolute;left:25px;top:45px;width:280px}
.footer-brand strong{font-family:"Plus Jakarta Sans",sans-serif;font-size:17px}
.footer-brand p{font-size:12px;line-height:19px;color:var(--muted);margin-top:16px}
.footer-col{position:absolute;top:45px}
.footer-col h6{font-size:12px;letter-spacing:.2em;font-weight:700;color:var(--ink-soft)}
.footer-col ul{list-style:none;margin-top:18px;display:flex;flex-direction:column;gap:10px;font-size:12px;color:var(--muted)}
.footer-col li{text-decoration:underline}
.footer-bottom{position:absolute;left:25px;right:25px;top:222px;border-top:1px solid var(--line);padding-top:30px;display:flex;justify-content:space-between;font-size:11px;color:#9ea1a5}
.footer-bottom .icons{display:flex;gap:20px}
</style>
</head>
<body>

<header class="nav">
  <span class="nav-brand">Vexorun.co</span>
  <nav class="nav-links">
    <a class="is-active" href="#">Find Games</a>
    <a href="#">Clubs</a>
    <a href="#">Tournaments</a>
    <a href="#">Coaches</a>
  </nav>
  <div class="nav-right">
    <svg width="18" height="18" viewBox="0 0 24 24" fill="#222"><path d="M12 22a2.5 2.5 0 0 0 2.5-2.5h-5A2.5 2.5 0 0 0 12 22zm7-6V11a7 7 0 0 0-5-6.7V3a2 2 0 0 0-4 0v1.3A7 7 0 0 0 5 11v5l-2 2v1h18v-1z"/></svg>
    <svg width="20" height="20" viewBox="0 0 24 24" fill="none" stroke="#222" stroke-width="2"><circle cx="12" cy="12" r="10"/><circle cx="12" cy="10" r="3"/><path d="M6.5 18.5a7 7 0 0 1 11 0"/></svg>
    <a class="btn btn-lime" href="#">Join Now</a>
  </div>
</header>

<section class="hero">
  <span class="hero-tag">THE FUTURE OF SPORT</span>
  <h1 class="hero-title heading">Let the Games Begin <span class="accent">&amp; Pick Your Challenge</span></h1>
  <p class="hero-text">The unified ecosystem to find games, manage clubs, and grow your coaching business. All in one place.</p>
  <div class="hero-actions">
    <a class="btn btn-lime" href="#">Join a Game</a>
    <a class="btn btn-grey" href="#">Register Your Club</a>
  </div>
  <div class="hero-tile tile-a" role="img" aria-label="Padel player hitting a shot on a blue court"></div>
  <div class="hero-tile tile-b" role="img" aria-label="Soccer players competing under stadium lights"></div>
  <div class="hero-tile tile-c" role="img" aria-label="Tennis player on a clay court"></div>
  <div class="hero-tile tile-d" role="img" aria-label="Pickleball paddle striking a ball"></div>
</section>

<section class="partners">
  <p class="partners-label">POWERING ELITE PERFORMANCE ACROSS</p>
  <div class="partners-list">
    <span>COURTLINE</span><span>PRIMEPADEL</span><span>ARENAVOLT</span><span>STRIKECLUBS</span><span>SETPOINT</span>
  </div>
</section>

<article class="card card-find">
  <div class="card-body">
    <svg class="card-icon" viewBox="0 0 24 24" fill="none" stroke="#3f5d00" stroke-width="2.2"><circle cx="11" cy="9" r="5"/><path d="M7 18l-3 3M15 13l2 2"/></svg>
    <h3 class="card-title">Find and Join Games Instantly</h3>
    <p class="card-text">Browse local games, match with players at your level, and jump onto the court without the back-and-forth messaging friction.</p>
  </div>
  <div class="tags"><span class="tag">MATCHMAKING</span><span class="tag">LIVE BOOKING</span></div>
  <div class="photo" role="img" aria-label="Two players high-fiving on an indoor padel court"></div>
</article>

<article class="card card-manage">
  <div class="card-body">
    <svg class="card-icon" viewBox="0 0 24 24" fill="#d4f000"><rect x="3" y="9" width="18" height="11" rx="2"/><rect x="5" y="4" width="4" height="5"/><rect x="15" y="4" width="4" height="5"/></svg>
    <h3 class="card-title">Management Reinvented</h3>
    <p class="card-text">Full control over players, classes, and payments. Automated filling of empty courts ensures zero downtime.</p>
  </div>
  <ul class="checks">
    <li><svg width="20" height="20" viewBox="0 0 20 20"><circle cx="10" cy="10" r="10" fill="#d4f000"/><path d="M6 10l3 3 5-6" stroke="#0e0f10" stroke-width="2" fill="none"/></svg>100% Automated Court Filling</li>
    <li><svg width="20" height="20" viewBox="0 0 20 20"><circle cx="10" cy="10" r="10" fill="#d4f000"/><path d="M6 10l3 3 5-6" stroke="#0e0f10" stroke-width="2" fill="none"/></svg>Integrated Payment Processing</li>
  </ul>
</article>

<article class="card card-coach">
  <div class="card-body">
    <svg class="card-icon" viewBox="0 0 24 24" fill="#3f5d00"><path d="M12 3L1 9l11 6 9-4.9V17h2V9z"/><path d="M5 13.2V17c0 1.7 3.1 3 7 3s7-1.3 7-3v-3.8l-7 3.8z"/></svg>
    <h3 class="card-title">Coach &amp; Earn Directly</h3>
    <p class="card-text">Launch lessons, manage your programs, and get paid instantly. Your entire business on one dashboard.</p>
  </div>
  <a class="btn" href="#">Start Coaching</a>
</article>

<article class="card card-create" role="img" aria-label="Tennis ball resting on a blue court in front of a modern clubhouse">
  <div class="caption">
    <h3>Create Games Without Friction</h3>
    <p>Set your rules, pick your level, and let Vexorun find the perfect opponents.</p>
  </div>
</article>

<section class="steps">
  <h2 class="section-title">Precision in 3 Steps</h2>
  <p class="section-sub">We've removed the hurdles. You focus on the performance.</p>
  <div class="step" style="left:27px">
    <div class="step-icon"><svg width="32" height="32" viewBox="0 0 24 24" fill="none" stroke="#3f5d00" stroke-width="2"><path d="M9 11V5a2 2 0 0 1 4 0v6l4 1a2 2 0 0 1 1.5 2.3L17.5 20H9l-3-5 1.5-1L9 15"/></svg></div>
    <h4>01. Select Sport</h4>
    <p>Choose from Padel, Tennis, Soccer or Pickleball across our partner network.</p>
  </div>
  <div class="step" style="left:425px">
    <div class="step-icon"><svg width="30" height="30" viewBox="0 0 24 24" fill="none" stroke="#3f5d00" stroke-width="2.4"><circle cx="10" cy="10" r="6"/><path d="M15 15l6 6"/></svg></div>
    <h4>02. Find or Create</h4>
    <p>Join an existing match or create your own challenge with custom settings.</p>
  </div>
  <div class="step" style="left:832px">
    <div class="step-icon is-lime"><svg width="34" height="34" viewBox="0 0 24 24" fill="none" stroke="#2f4700" stroke-width="2"><path d="M4 20l6-12 6 6z"/><path d="M14 4v2M18 6l-1.5 1.5M20 10h-2"/></svg></div>
    <h4>03. Play &amp; Compete</h4>
    <p>Show up, play hard, and track your performance directly on Vexorun.</p>
  </div>
</section>

<section class="arena">
  <h2 class="section-title">Choose Your Arena</h2>
  <p class="section-sub">Curated sport experiences for every athlete.</p>
  <a class="arena-link" href="#">Explore All Sports <svg width="14" height="14" viewBox="0 0 24 24" fill="none" stroke="#3f5d00" stroke-width="2.5"><path d="M4 12h16M14 6l6 6-6 6"/></svg></a>
  <div class="sport" style="left:0">
    <div class="sport-photo" role="img" aria-label="Padel player swinging on a blue court" style="background:linear-gradient(170deg,#2a3a2f,#3b6a44 45%,#2a5fb0)"><span class="sport-badge">PRO LEVEL</span></div>
    <h5>Padel</h5><p>The fastest growing racket sport.</p>
  </div>
  <div class="sport" style="left:296px">
    <div class="sport-photo" role="img" aria-label="Two pickleball players at the net outdoors" style="background:linear-gradient(170deg,#8fb6d6,#5f8f64 45%,#2d6fb5)"><span class="sport-badge">SOCIAL</span></div>
    <h5>Pickleball</h5><p>Strategic, social, and addictive.</p>
  </div>
  <div class="sport" style="left:591px">
    <div class="sport-photo" role="img" aria-label="Tennis ball on an orange clay court line" style="background:linear-gradient(170deg,#b85a2a,#d0703a 55%,#c2612e)"><span class="sport-badge">CLASSIC</span></div>
    <h5>Tennis</h5><p>Tradition meets performance.</p>
  </div>
  <div class="sport" style="left:887px">
    <div class="sport-photo" role="img" aria-label="Soccer player under floodlights at night" style="background:linear-gradient(180deg,#0c1a22,#1d3a4a 50%,#2f5a34)"><span class="sport-badge">INTENSE</span></div>
    <h5>Soccer</h5><p>Gather your squad for the match.</p>
  </div>
</section>

<section class="cta">
  <h2>Ready to Pick<br>Your Challenge?</h2>
  <p>Join thousands of athletes already dominating their local courts and pitches.</p>
  <a class="btn btn-lime" href="#">Join Now</a>
</section>

<footer class="footer">
  <div class="footer-brand">
    <strong>Vexorun.co</strong>
    <p>Elevate precision in sport ecosystem. Connecting players, clubs, and coaches worldwide.</p>
  </div>
  <div class="footer-col" style="left:318px"><h6>PLAYERS</h6><ul><li>Padel</li><li>Pickleball</li><li>Tennis</li><li>Locations</li></ul></div>
  <div class="footer-col" style="left:614px"><h6>PARTNERS</h6><ul><li>Register Club</li><li>Coaching Program</li><li>Tournaments</li></ul></div>
  <div class="footer-col" style="left:910px"><h6>COMPANY</h6><ul><li>About Us</li><li>Terms</li><li>Help Center</li></ul></div>
  <div class="footer-bottom">
    <span>© 2024 Vexorun.co · Kinetic Precision in Sport</span>
    <span class="icons">
      <svg width="16" height="16" viewBox="0 0 24 24" fill="none" stroke="#6d6f72" stroke-width="2"><circle cx="12" cy="12" r="10"/><path d="M2 12h20M12 2c3 3 3 17 0 20M12 2c-3 3-3 17 0 20"/></svg>
      <svg width="16" height="16" viewBox="0 0 24 24" fill="none" stroke="#6d6f72" stroke-width="2"><circle cx="6" cy="12" r="2.5"/><circle cx="18" cy="6" r="2.5"/><circle cx="18" cy="18" r="2.5"/><path d="M8 11l8-4M8 13l8 4"/></svg>
    </span>
  </div>
</footer>

</body>
</html>
```